Eye-Catching, Direct Marketing Residential Painting Flyer!

I am run a residential painting business and am looking for a flyer to be designed to mailout to potential customers.
I want the copy/wording to be designed similar to this flyer.

It's important that the person reading the flyer gets the benefits we're promoting which is why I want the wording/copy to be almost identical to the flyer attached.

However, the structure will be different. The flyer will be a postcard thick, 5 x11.5.
Double sided.

The name of the company is Brightwall Coaters.

I would also like the prominent colour to either be light green or orange.

Target Market(s)

Home Owners between the age of 45-80.

Industry/Entity Type

Painting And Decorating

Font styles to use
Serif

Colors
f68d4d
faa54b
f78f20
f37122
9bcb3c
abd037
cadf82

Requirements
Must have
• Excellent Eye-Catching Design
• Benefits Visibly Promoted
• Action Taking Incentive- Call Now for FREE Window Cleaning and FREE Painting Estimate
Should not have
• Crowded wording

```html
<!DOCTYPE html>
<html lang="en">
<head>
<meta charset="utf-8">
<title>Brightwall Coaters – Postcard</title>
<link href="https://fonts.googleapis.com/css2?family=Lilita+One&family=Lato:wght@400;700;900&family=Roboto+Condensed:wght@400;700&display=swap" rel="stylesheet">
<style>
  :root{
    --orange:#f37122;
    --orange-mid:#f78f20;
    --orange-soft:#f68d4d;
    --orange-light:#faa54b;
    --green:#9bcb3c;
    --green-light:#abd037;
    --ink:#3a3a3a;
    --paper:#ffffff;
    --stage:#e6e6e6;
  }
  *{box-sizing:border-box;margin:0;padding:0}
  html,body{width:1200px;height:801px;overflow:hidden;background:var(--stage)}
  .canvas{position:relative;width:1200px;height:801px}
  .card{position:absolute;left:269px;width:662px;height:287px;background:var(--paper);overflow:hidden;box-shadow:0 3px 10px rgba(0,0,0,.25)}
  .card--front{top:98px}
  .card--back{top:415px}
  .card-shapes{position:absolute;inset:0}

  /* Front */
  .brand{position:absolute;left:0;width:242px;top:24px;text-align:center}
  .brand-dot{display:block;margin:0 auto 4px;width:22px;height:22px;border-radius:50%;background:var(--paper)}
  .brand-name{font-family:"Lato",sans-serif;font-weight:900;font-size:14px;letter-spacing:.5px;color:var(--paper);display:inline-block;border-bottom:2px solid var(--paper);padding-bottom:1px}
  .headline{position:absolute;left:0;width:242px;top:80px;text-align:center;font-family:"Lilita One",sans-serif;font-size:27px;line-height:31.5px;color:var(--orange-light)}
  .headline .accent{color:var(--paper)}

  .offer{position:absolute;left:252px;width:190px;top:22px;text-align:center;font-family:"Lato",sans-serif;color:var(--ink)}
  .offer-tag{position:relative;height:26px;margin:0 auto 18px;width:176px}
  .offer-tag svg{position:absolute;inset:0}
  .offer-tag span{position:relative;display:block;line-height:26px;font-family:"Lilita One",sans-serif;font-size:15px;color:var(--orange-light);letter-spacing:.3px}
  .offer-item{font-size:10px;line-height:12.5px;font-weight:700}
  .offer-item .hl{color:var(--orange);font-size:11.5px}
  .offer-item .hl-sm{color:var(--orange);font-size:10px}
  .offer-rule{width:120px;height:1px;background:#bdbdbd;margin:9px auto 10px;box-shadow:0 3px 0 #e2e2e2}

  .cta-bar{position:absolute;left:0;top:258px;width:560px;height:29px;background:var(--green);color:var(--paper);font-family:"Roboto Condensed",sans-serif;font-size:16.5px;line-height:29px;padding-left:19px}

  /* Back */
  .tag{position:absolute;left:3px;width:120px;height:18px}
  .tag svg{position:absolute;inset:0}
  .tag span{position:relative;display:block;text-align:center;line-height:18px;font-family:"Lilita One",sans-serif;font-size:13px;color:var(--orange)}
  .tag--problem{top:13px}
  .tag--solution{top:138px}
  .copy{position:absolute;left:22px;width:200px;font-family:"Lato",sans-serif;font-weight:900;font-size:9px;line-height:12px;color:var(--paper)}
  .copy--problem{top:40px}
  .copy--solution{top:164px}
  .deck-photo{position:absolute;left:22px;top:67px;width:152px;height:65px;border:2px solid var(--paper);border-radius:6px;background:linear-gradient(160deg,#b98a5c,#8a5d3a 60%,#6e4a2e)}
  .contact{position:absolute;left:23px;top:206px;font-family:"Lilita One",sans-serif;color:var(--orange)}
  .contact-label{font-size:14px;line-height:17px}
  .contact-phone{font-size:21px;line-height:24px;letter-spacing:.5px}
  .contact-web{font-size:18px;line-height:20px}
  .stamp{position:absolute;left:572px;top:26px;width:58px;height:58px;border:1.5px solid #555}
  .address-line{position:absolute;left:438px;width:192px;height:0;border-top:1.2px solid #555}
</style>
</head>
<body>
<div class="canvas">

  <!-- Front side -->
  <section class="card card--front">
    <svg class="card-shapes" width="662" height="287" viewBox="0 0 662 287">
      <defs>
        <linearGradient id="wallTone" x1="0" y1="0" x2="0" y2="1">
          <stop offset="0" stop-color="#c79b78"/>
          <stop offset=".55" stop-color="#d6b79b"/>
          <stop offset=".6" stop-color="#eeeae6"/>
          <stop offset="1" stop-color="#e2ddd8"/>
        </linearGradient>
        <linearGradient id="deckTone" x1="0" y1="0" x2="1" y2="1">
          <stop offset="0" stop-color="#b9ad8e"/>
          <stop offset=".5" stop-color="#c9b48a"/>
          <stop offset="1" stop-color="#8f8a78"/>
        </linearGradient>
        <linearGradient id="roomTone" x1="0" y1="0" x2="1" y2="1">
          <stop offset="0" stop-color="#d9d6d2"/>
          <stop offset=".6" stop-color="#f1efec"/>
          <stop offset="1" stop-color="#c9c3bc"/>
        </linearGradient>
        <linearGradient id="stairTone" x1="0" y1="0" x2="1" y2="1">
          <stop offset="0" stop-color="#aebbb8"/>
          <stop offset=".5" stop-color="#7f8d8b"/>
          <stop offset="1" stop-color="#5e6b6a"/>
        </linearGradient>
      </defs>
      <ellipse cx="20" cy="150" rx="250" ry="270" fill="none" stroke="var(--orange-light)" stroke-width="3"/>
      <ellipse cx="20" cy="150" rx="240" ry="262" fill="var(--orange)"/>
      <circle cx="712" cy="40" r="212" fill="url(#wallTone)" stroke="var(--orange)" stroke-width="4" role="img" aria-label="Photo of a freshly painted interior wall with white wainscoting"/>
      <circle cx="606" cy="212" r="84" fill="url(#deckTone)" stroke="var(--orange)" stroke-width="4" role="img" aria-label="Photo of weathered deck boards before staining"/>
      <circle cx="490" cy="98" r="62" fill="url(#roomTone)" stroke="var(--orange)" stroke-width="4" role="img" aria-label="Photo of a bright white painted room corner"/>
      <circle cx="522" cy="193" r="66" fill="url(#stairTone)" stroke="var(--orange)" stroke-width="4" role="img" aria-label="Photo of freshly painted grey deck stairs"/>
    </svg>

    <div class="brand">
      <span class="brand-dot"></span>
      <span class="brand-name">BRIGHTWALL COATERS</span>
    </div>
    <h1 class="headline">
      We make your<br>home look<br>
      <span class="accent">CLEAN, FRESH</span><br>
      <span class="accent">&amp; Beautiful</span><br>again!
    </h1>

    <div class="offer">
      <div class="offer-tag">
        <svg width="176" height="26" viewBox="0 0 176 26"><polygon points="2,3 12,1 170,2 176,6 166,9 174,13 168,18 174,23 8,25 0,20 7,15 1,11 8,7" fill="var(--orange)"/></svg>
        <span>SPECIAL OFFER!</span>
      </div>
      <p class="offer-item">If you are one of the<br>
        <span class="hl">first 17 exterior projects</span><br>
        that book with us, you will<br>receive a complimentary<br>
        <span class="hl-sm">window cleaning!</span></p>
      <div class="offer-rule"></div>
      <p class="offer-item">If you are one of the<br>
        <span class="hl">first 13 exterior projects</span><br>
        that book with us, you will receive<br>a complimentary<br>
        <span class="hl-sm">interior design consultation by a<br>professional interior designer!</span></p>
    </div>

    <div class="cta-bar">Call Now for FREE Window Cleaning and FREE Painting Estimate</div>
  </section>

  <!-- Back side -->
  <section class="card card--back">
    <svg class="card-shapes" width="662" height="287" viewBox="0 0 662 287">
      <defs>
        <clipPath id="innerArc"><ellipse cx="20" cy="144" rx="222" ry="262"/></clipPath>
      </defs>
      <ellipse cx="20" cy="144" rx="252" ry="278" fill="none" stroke="var(--orange-light)" stroke-width="3"/>
      <ellipse cx="20" cy="144" rx="242" ry="270" fill="var(--orange)"/>
      <rect x="0" y="191" width="300" height="100" fill="var(--paper)" clip-path="url(#innerArc)"/>
    </svg>

    <div class="tag tag--problem">
      <svg width="120" height="18" viewBox="0 0 120 18"><polygon points="0,3 10,1 114,2 120,5 112,8 119,12 113,16 6,17 0,14 6,10 1,7" fill="var(--paper)"/></svg>
      <span>Problem:</span>
    </div>
    <p class="copy copy--problem">Your exterior semi-transparent deck, fence<br>or siding is peeling, chipping or faded.</p>
    <div class="deck-photo" role="img" aria-label="Photo of a worn wooden deck with a stain can and brush"></div>

    <div class="tag tag--solution">
      <svg width="120" height="18" viewBox="0 0 120 18"><polygon points="0,3 10,1 114,2 120,5 112,8 119,12 113,16 6,17 0,14 6,10 1,7" fill="var(--paper)"/></svg>
      <span>Solution:</span>
    </div>
    <p class="copy copy--solution">A fresh coat of stain to protect the wood and<br>make it look clean, fresh and beautiful!</p>

    <div class="contact">
      <p class="contact-label">Free Estimates:</p>
      <p class="contact-phone">000 - 000 - 0000</p>
      <p class="contact-web">brightwallcoaters.com</p>
    </div>

    <div class="stamp"></div>
    <div class="address-line" style="top:199px"></div>
    <div class="address-line" style="top:226px"></div>
    <div class="address-line" style="top:253px"></div>
  </section>

</div>
</body>
</html>
```